Harwick Lending Hard Money Lender

We are looking for this flyer to be redesigned. We would like it to be even more simple than the attached design. No photos, no exclamation points, a 3-4 color palate maximum. We would do not want any graphics around the "Harwick Lending" logo.

```html
<!DOCTYPE html>
<html lang="en">
<head>
<meta charset="UTF-8">
<title>Harwick Lending – Hard Money Loans</title>
<link href="https://fonts.googleapis.com/css2?family=Inter:ital,wght@0,400;0,500;0,700;0,800;1,400&family=Oswald:wght@300&display=swap" rel="stylesheet">
<style>
  :root {
    --backdrop: #eeeeee;
    --navy: #1a2436;
    --white: #f4f4f6;
    --silver: #b3b4b8;
    --phone-grey: #c9cacd;
  }
  * { margin: 0; padding: 0; box-sizing: border-box; }
  html, body {
    width: 1150px;
    height: 1200px;
    overflow: hidden;
    background: var(--backdrop);
  }
  .flyer {
    position: absolute;
    left: 160px;
    top: 36px;
    width: 830px;
    height: 1128px;
    overflow: hidden;
    background: var(--navy);
    color: var(--white);
    font-family: "Inter", sans-serif;
  }
  .brand-name {
    position: absolute;
    left: 152px;
    top: 500px;
    transform: translate(-50%, -50%) rotate(-90deg);
    white-space: nowrap;
    font-weight: 400;
    font-size: 50px;
    letter-spacing: 4px;
    text-transform: uppercase;
    color: var(--white);
  }
  .content {
    position: absolute;
    left: 306px;
    top: 0;
    width: 500px;
  }
  .headline {
    position: absolute;
    top: 140px;
    left: 0;
    font-weight: 800;
    font-size: 87px;
    line-height: 74px;
    letter-spacing: -0.5px;
    white-space: nowrap;
  }
  .headline span { display: block; }
  .headline .accent { color: var(--silver); }
  .divider {
    position: absolute;
    top: 400px;
    left: -8px;
    width: 366px;
    height: 2px;
    background: var(--white);
  }
  .rate {
    position: absolute;
    top: 420px;
    left: 0;
    font-family: "Oswald", sans-serif;
    font-weight: 300;
    font-size: 50px;
    line-height: 60px;
    white-space: nowrap;
  }
  .loan-types {
    position: absolute;
    top: 512px;
    left: 0;
    list-style: none;
  }
  .loan-types li {
    display: flex;
    align-items: center;
    height: 43px;
    font-size: 28px;
    font-weight: 500;
    white-space: nowrap;
  }
  .loan-types svg {
    width: 26px;
    height: 26px;
    margin-right: 24px;
    flex-shrink: 0;
  }
  .terms {
    position: absolute;
    top: 689px;
    left: 0;
    font-size: 20px;
    font-weight: 700;
    line-height: 32px;
    white-space: nowrap;
  }
  .terms em { font-weight: 400; font-style: italic; }
  .phone {
    position: absolute;
    top: 793px;
    left: -2px;
    font-size: 65px;
    font-weight: 800;
    line-height: 74px;
    color: var(--phone-grey);
    white-space: nowrap;
  }
  .contact {
    position: absolute;
    top: 872px;
    left: 0;
    font-size: 20px;
    font-weight: 700;
    line-height: 32px;
    white-space: nowrap;
  }
</style>
</head>
<body>
  <main class="flyer">
    <div class="brand-name">Harwick Lending</div>

    <section class="content">
      <h1 class="headline">
        <span>HARD</span>
        <span class="accent">MONEY</span>
        <span>LOANS</span>
      </h1>
      <div class="divider"></div>
      <p class="rate">RATES FROM 8%</p>

      <ul class="loan-types">
        <li><svg viewBox="0 0 24 24"><path d="M3 12.5l6 6L21 6" fill="none" stroke="#b3b4b8" stroke-width="4" stroke-linecap="round" stroke-linejoin="round"/></svg>Fix &amp; Flip Loans</li>
        <li><svg viewBox="0 0 24 24"><path d="M3 12.5l6 6L21 6" fill="none" stroke="#b3b4b8" stroke-width="4" stroke-linecap="round" stroke-linejoin="round"/></svg>Commercial Loans</li>
        <li><svg viewBox="0 0 24 24"><path d="M3 12.5l6 6L21 6" fill="none" stroke="#b3b4b8" stroke-width="4" stroke-linecap="round" stroke-linejoin="round"/></svg>Hard Money Loans</li>
      </ul>

      <div class="terms">
        <p>Same-Day Approval</p>
        <p>No Processing, Appraisal, or Extra Fees</p>
        <p>100% Financing <em>(w/ Additional Collateral)</em></p>
      </div>

      <p class="phone">303.555.0148</p>

      <div class="contact">
        <p>hello@harwicklending.com</p>
        <p>http://harwicklending.com</p>
      </div>
    </section>
  </main>
</body>
</html>
```